Online Shop Marta

We need a web design for an online shop, called "Orvil Dapt Jewels". The shop should have an extraordinary, elegant look, as shown in the Quincefield Advertising Picture in our Briefing.pdf (attached). Please have a look at our Briefing regarding website colours, background ideas, and elements to be included. The online shop is about professional jewellery design pieces, where each piece is handmade of high quality materials, also unique pieces and unique editions possible. It should attract extraordinary people and visualize that its a very individual and unique design jewellery. You can get an idea of whom it should attract by reading our target group. Colours to be used are jewellery-Velvet red, Black / anthracite, exclusive colours, silverish-white, bronze-brown and golden.

Please play around when designing with the image pictures we attach, preferably more vertical pictures, no panoramic pictures like in Brontel Shop. Also include the BLACK logo of orvil dapt. We include the SITEMAP in the briefing and also another folder with product pictures you can use for the draft.

Regarding Functions, the store will have the SAME (technical) functions as this page:http://www.brontel-shop.eu/ - using the "most famous" products/categories for the starting page, going into individual product pages by clicking these images and then leading to a detailed page for one product only.

Target Market(s)

Jewellery-lovers, who appreciate extraordinary things, creative economy/fashion-industries, stylists, Style consultants, outfitter, theatres, operas, production sites, Cocktail-, Dinner and Bridefashion, exclusive traditional costume stores, dancesports and tango argento dancers

Industry/Entity Type

Shop

Requirements
Must have
• Must include:
• Colours as per briefing
• Background ideas/images as per briefing/pictures sent
• Sitemap as per briefing
• Social buttons
• Logo
• Design for 3 pages: Starting page showing big images, attractive design and the 4 popular categories
• Subpage with different products of one category (i.e. bracelets)
• Detail page with one individual product only
Should not have
• no fresh, playful colours like yellow, orange, green, blue
• no cheap design, no panorama pictures

```html
<!DOCTYPE html>
<html lang="en">
<head>
<meta charset="utf-8">
<title>Orvil Dapt Jewels</title>
<link rel="stylesheet" href="https://fonts.googleapis.com/css2?family=Cinzel:wght@400;700&family=Source+Sans+3:wght@300;400;600&display=swap">
<style>
:root{
  --page:#1f1e1f;
  --wood-base:#2e2926;
  --wood-light:#3a3430;
  --wood-seam:#181514;
  --top-bar:#3a3939;
  --gold-light:#f2c860;
  --gold-dark:#d59f36;
  --gold-text:#d4a13f;
  --nav-ink:#3b2a10;
  --card:#2a292b;
  --card-band:#333236;
  --card-border:#3a393c;
  --text:#e9e6e2;
  --muted:#a9a6a3;
  --line:#3b3a3d;
}
*{box-sizing:border-box;margin:0;padding:0}
html,body{width:1003px;height:1200px;overflow:hidden;background:var(--page)}
.canvas{position:relative;width:1003px;height:1200px;overflow:hidden;background:var(--page);
  font-family:"Source Sans 3",sans-serif;color:var(--text)}
.abs{position:absolute}

/* wooden plank backdrop, fading into the page */
.wood{left:0;top:0;width:1003px;height:440px;
  background:
    linear-gradient(180deg,rgba(31,30,31,0) 0,rgba(31,30,31,0) 45%,var(--page) 100%),
    repeating-linear-gradient(90deg,var(--wood-seam) 0,var(--wood-seam) 2px,transparent 2px,transparent 96px),
    repeating-linear-gradient(90deg,rgba(255,255,255,.03) 0,rgba(255,255,255,.03) 30px,rgba(0,0,0,.06) 30px,rgba(0,0,0,.06) 58px,rgba(255,255,255,.02) 58px,rgba(255,255,255,.02) 96px),
    linear-gradient(90deg,var(--wood-base),var(--wood-light) 50%,var(--wood-base))}
.top-bar{left:0;top:0;width:1003px;height:6px;background:var(--top-bar)}

/* header */
.brand{left:0;width:1003px;top:30px;text-align:center;color:var(--text)}
.brand-name{font-size:42px;font-weight:400;letter-spacing:.5px;line-height:1}
.brand-sub{font-size:22px;margin-top:14px;line-height:1}
.brand-sub span{font-size:11px;vertical-align:4px;margin:0 6px}
.social{left:90px;top:85px;display:flex;gap:2px}
.social-btn{width:24px;height:24px;border-radius:50%;background:#f4f2ee;color:#1f1e1f;
  font-size:12px;font-weight:600;display:flex;align-items:center;justify-content:center}
.cart{left:817px;top:33px;width:92px;height:34px;border:1px solid #57524d;border-radius:17px;
  background:#201e1e;display:flex;align-items:center;justify-content:center;gap:5px;font-size:13px}
.search{left:713px;top:84px;width:203px;height:27px;border:1px solid #57524d;border-radius:3px;
  background:#1e1c1c;display:flex;align-items:center;justify-content:space-between;padding:0 8px 0 10px;
  font-size:11px;font-style:italic;color:#bdb8b3}

/* nav */
.nav{left:85px;top:125px;width:832px;height:40px;
  background:linear-gradient(180deg,var(--gold-light),var(--gold-dark));
  display:flex;align-items:center;justify-content:center;gap:20px;
  font-family:"Cinzel",serif;font-size:15px;color:var(--nav-ink);letter-spacing:.5px;text-transform:uppercase}
.nav .sep{font-size:10px}

/* hero */
.hero{left:85px;top:165px;width:832px;height:359px;
  background:
    linear-gradient(90deg,rgba(25,18,22,.65) 0,rgba(25,18,22,0) 20%,rgba(25,18,22,0) 80%,rgba(25,18,22,.65) 100%),
    linear-gradient(180deg,#3e2f3a 0,#5a4350 22%,#6a5448 48%,#86735a 72%,#6e5d4c 100%)}
.hero-title{left:85px;top:298px;width:832px;text-align:center;font-family:"Cinzel",serif;font-weight:700;
  font-size:38px;line-height:46px;color:#f6efe6;text-shadow:0 2px 4px rgba(0,0,0,.6)}

/* categories */
.cat{width:268px;height:156px;top:541px;background:var(--card);border:1px solid var(--card-border);overflow:hidden}
.cat-img{height:96px}
.cat-band{position:absolute;left:0;right:0;top:96px;bottom:0;background:var(--card-band);text-align:center}
.cat-title{font-family:"Cinzel",serif;font-weight:700;font-size:21px;margin-top:9px;line-height:1;text-shadow:0 1px 2px rgba(0,0,0,.5)}
.cat-text{font-size:11px;margin-top:6px;color:#dcd8d3}

/* products */
.section-title{left:85px;top:737px;font-family:"Cinzel",serif;font-weight:700;font-size:21px;color:var(--gold-text)}
.product{top:777px;width:202px;height:241px;background:var(--card);border:1px solid var(--card-border)}
.product-img{height:132px}
.product-body{padding:15px 0 0 17px}
.product-name{font-size:17px;font-weight:400;line-height:1}
.product-text{font-size:10px;color:var(--muted);line-height:15px;margin-top:5px;font-weight:300}
.product-price{font-size:17px;font-weight:600;color:var(--gold-text);margin-top:5px}

/* footer */
.divider{left:85px;top:1089px;width:832px;height:1px;background:var(--line)}
.footer-links{left:87px;top:1123px;font-size:12px;color:#dcd8d3}
.footer-links span{margin:0 5px;color:#8a8783}
.copyright{left:87px;top:1151px;font-size:10px;color:#8a8783}
.payments{left:747px;top:1123px;display:flex;gap:4px}
.pay{width:36px;height:23px;background:#f2f0ec;color:#1f1e1f;font-size:8px;font-weight:600;
  display:flex;align-items:center;justify-content:center}
</style>
</head>
<body>
<div class="canvas">
  <div class="abs wood"></div>
  <div class="abs top-bar"></div>

  <header>
    <div class="abs brand">
      <div class="brand-name">Orvil Dapt</div>
      <div class="brand-sub"><span>♦</span>Jewels<span>♦</span></div>
    </div>
    <div class="abs social" aria-label="Social links">
      <div class="social-btn" title="Kestova">K</div>
      <div class="social-btn" title="Murlo">M</div>
      <div class="social-btn" title="Rindel">R</div>
      <div class="social-btn" title="Soplan">S</div>
    </div>
    <div class="abs cart">My Cart
      <svg width="20" height="16" viewBox="0 0 20 16" fill="none" stroke="#f0ede8" stroke-width="1.4">
        <path d="M1 2h3l2 9h10l2-7H5"/><circle cx="8" cy="14" r="1.3"/><circle cx="15" cy="14" r="1.3"/>
      </svg>
    </div>
    <div class="abs search">Search here..
      <svg width="15" height="15" viewBox="0 0 15 15" fill="none" stroke="#f0ede8" stroke-width="1.8">
        <circle cx="6.5" cy="6.5" r="5"/><path d="M10 10l4 4"/>
      </svg>
    </div>
  </header>

  <nav class="abs nav">
    <span>Home</span><span class="sep">♦</span>
    <span>Online Shop</span><span class="sep">♦</span>
    <span>Info &amp; Facts</span><span class="sep">♦</span>
    <span>Partner</span><span class="sep">♦</span>
    <span>About Me</span><span class="sep">♦</span>
    <span>Contact</span>
  </nav>

  <section>
    <div class="abs hero" role="img" aria-label="Photo of a woman in a lavish gown on stone palace steps before ornate iron gates"></div>
    <svg class="abs" style="left:104px;top:305px" width="34" height="77" viewBox="0 0 34 77" fill="none" stroke="#e8e2da" stroke-width="1.2">
      <path d="M33 1L1 38l32 38"/>
    </svg>
    <svg class="abs" style="left:869px;top:305px" width="34" height="77" viewBox="0 0 34 77" fill="none" stroke="#e8e2da" stroke-width="1.2">
      <path d="M1 1l32 37L1 76"/>
    </svg>
    <h1 class="abs hero-title">A DREAM JEWELLERY<br>COLLECTION HERE..</h1>
  </section>

  <section>
    <div class="abs cat" style="left:84px">
      <div class="cat-img" role="img" aria-label="Photo of a black beaded collar necklace" style="background:radial-gradient(ellipse at 50% 20%,#5a5a5e 0,#38373b 45%,#19191b 100%)"></div>
      <div class="cat-band"><div class="cat-title">BEST DESIGNS</div><div class="cat-text">Fusce tellus Sed metus augue convallis vehicula</div></div>
    </div>
    <div class="abs cat" style="left:368px">
      <div class="cat-img" role="img" aria-label="Photo of crystal and gold beaded bracelets" style="background:linear-gradient(120deg,#6a6864 0,#b8b4aa 28%,#8e7f52 52%,#c2a550 72%,#4a4536 100%)"></div>
      <div class="cat-band"><div class="cat-title">LATEST EDITION</div><div class="cat-text">Fusce tellus Sed metus augue convallis vehicula</div></div>
    </div>
    <div class="abs cat" style="left:651px">
      <div class="cat-img" role="img" aria-label="Photo of a pearl and crystal brooch" style="background:radial-gradient(ellipse at 45% 55%,#b6aca2 0,#7c746e 35%,#3e3d42 70%,#26252a 100%)"></div>
      <div class="cat-band"><div class="cat-title">LOVING COLLECTION</div><div class="cat-text">Fusce tellus Sed metus augue convallis vehicula</div></div>
    </div>
  </section>

  <section>
    <h2 class="abs section-title">LATEST PRODUCT</h2>
    <div class="abs product" style="left:82px">
      <div class="product-img" role="img" aria-label="Photo of a black and gold beaded necklace" style="background:radial-gradient(ellipse at 50% 55%,#2a292d 0,#4a494f 45%,#3a393e 100%)"></div>
      <div class="product-body"><div class="product-name">Product Name</div>
        <div class="product-text">Fusce tellus Sed metus augue conval-<br>lis vehicula convallis et</div>
        <div class="product-price">£ 60.00</div></div>
    </div>
    <div class="abs product" style="left:294px">
      <div class="product-img" role="img" aria-label="Photo of a pearl necklace on a fine wire" style="background:radial-gradient(ellipse at 52% 55%,#d8d4cc 0,#8a888c 22%,#4e4d53 55%,#36353a 100%)"></div>
      <div class="product-body"><div class="product-name">Product Name</div>
        <div class="product-text">Fusce tellus Sed metus augue conval-<br>lis vehicula convallis et</div>
        <div class="product-price">£ 70.00</div></div>
    </div>
    <div class="abs product" style="left:505px">
      <div class="product-img" role="img" aria-label="Photo of a woven silver beaded pendant" style="background:radial-gradient(ellipse 30% 50% at 50% 60%,#9c9a98 0,#5c5b5e 50%,#232226 100%)"></div>
      <div class="product-body"><div class="product-name">Product Name</div>
        <div class="product-text">Fusce tellus Sed metus augue conval-<br>lis vehicula convallis et</div>
        <div class="product-price">£ 55.00</div></div>
    </div>
    <div class="abs product" style="left:717px">
      <div class="product-img" role="img" aria-label="Photo of a gold beaded necklace with diamond-shaped drops" style="background:radial-gradient(ellipse at 50% 60%,#7c6a44 0,#4e4a4c 40%,#2c2b32 100%)"></div>
      <div class="product-body"><div class="product-name">Product Name</div>
        <div class="product-text">Fusce tellus Sed metus augue conval-<br>lis vehicula convallis et</div>
        <div class="product-price">£ 70.00</div></div>
    </div>
  </section>

  <footer>
    <div class="abs divider"></div>
    <div class="abs footer-links">Home<span>|</span>Online Shop<span>|</span>Info &amp; Facts<span>|</span>Partner<span>|</span>About me<span>|</span>Contact</div>
    <div class="abs copyright">© 2013 Company Name. All right reserved</div>
    <div class="abs payments" aria-label="Accepted payment cards">
      <div class="pay">Cardora</div>
      <div class="pay">Velia</div>
      <div class="pay">Amberline</div>
      <div class="pay">Distro</div>
    </div>
  </footer>

</div>
</body>
</html>
```